Commercial and Residential Paint Contractor needs website

We need a website for our residential painting, multi-family painting and commercial painting company. We paint interior and exterior of houses, apartments and commercial buildings. I would like an about us page, residential page, multi family page, commercial page and contact us. Need keywords added to website for seo opitimazation. I like this website https://www.velmorandhalestudio.com/

Target Market(s)

General Contractors and commercial property managers

Coding

Coded - Design and coding required

Number of Pages Required

5+ page

Font styles to use
Sans Serif

Requirements
Must have
• I need SEO keywords on pages

```html
<!DOCTYPE html>
<html lang="en">
<head>
<meta charset="utf-8">
<title>Halvern Painting — Our Services</title>
<link rel="stylesheet" href="https://fonts.googleapis.com/css2?family=Roboto:wght@400;500;700;900&display=swap">
<style>
:root{
  --navy:#0f4a8a;
  --navy-deep:#143c6b;
  --navy-field:#1d4f86;
  --red:#c8202f;
  --ink:#111111;
  --text:#333333;
  --muted:#555555;
  --faint:#f1f1f1;
  --white:#ffffff;
}
*{box-sizing:border-box;margin:0;padding:0}
html,body{width:1200px;height:2535px;overflow:hidden}
body{position:relative;font-family:'Roboto',sans-serif;color:var(--text);background:var(--white)}
.abs{position:absolute}

.topbar{left:0;top:0;width:1200px;height:35px;background:var(--navy);color:#dfe8f3;font-size:12.5px}
.topbar .item{position:absolute;top:10px;display:flex;align-items:center;gap:8px}
.topbar svg{fill:#dfe8f3}
.social-dot{width:11px;height:11px;border-radius:50%;background:#dfe8f3;display:inline-block}

.nav{left:0;top:35px;width:1200px;height:84px;background:var(--white)}
.brand{position:absolute;left:98px;top:24px;font-size:24px;font-weight:900;color:var(--navy);letter-spacing:.5px;display:flex;align-items:center;gap:8px}
.brand .mark{width:12px;height:12px;background:var(--red)}
.menu{position:absolute;left:356px;top:34px;display:flex;gap:27px;font-size:13.5px;font-weight:500;color:var(--ink)}
.estimate{position:absolute;left:939px;top:20px;width:173px;height:45px;border:1px solid var(--red);color:var(--red);font-size:12.5px;font-weight:500;display:flex;align-items:center;justify-content:center;border-radius:2px}

.hero{left:0;top:119px;width:1200px;height:273px;background:linear-gradient(180deg,#2a2c30,#3b3d41 60%,#2e3033)}
.hero h1{position:absolute;left:86px;top:90px;font-size:40px;font-weight:700;color:var(--white)}
.crumbs{position:absolute;left:86px;top:152px;font-size:14px;color:#e8e8e8;display:flex;gap:10px}
.crumbs b{font-weight:500;color:var(--white)}

.num{font-size:130px;font-weight:900;color:var(--faint);line-height:1;letter-spacing:-4px}
.photo{box-shadow:0 12px 28px rgba(0,0,0,.22)}
.svc h2{font-size:31px;font-weight:700;color:var(--ink)}
.svc .lead{margin-top:22px;font-size:17.5px;line-height:26px;color:var(--text);width:440px}
.svc .body{margin-top:16px;font-size:14px;line-height:26.5px;color:var(--muted);width:445px}
.btn{margin-top:34px;width:164px;height:52px;border:1px solid var(--red);color:var(--red);font-size:13.5px;font-weight:700;display:flex;align-items:center;justify-content:center;gap:10px;border-radius:2px}

.cta{left:0;top:1880px;width:1200px;height:169px;background:var(--red)}
.cta h3{position:absolute;left:86px;top:66px;font-size:35px;font-weight:700;color:var(--white)}
.quote{position:absolute;left:947px;top:62px;width:167px;height:51px;background:var(--white);color:var(--navy-deep);font-size:13.5px;font-weight:500;display:flex;align-items:center;justify-content:center;gap:10px;box-shadow:0 6px 14px rgba(0,0,0,.2)}

.footer{left:0;top:2049px;width:1200px;height:486px;background:linear-gradient(135deg,#163e6e,#12355f 60%,#1a416f)}
.flogo{position:absolute;left:80px;top:70px;width:263px;height:97px;background:var(--white);display:flex;align-items:center;justify-content:center;gap:10px;font-size:36px;font-weight:900;color:var(--navy)}
.flogo .mark{width:16px;height:16px;background:var(--red)}
.fabout{position:absolute;left:80px;top:196px;width:290px;font-size:14px;line-height:25px;color:#e4ebf4}
.fsocial{position:absolute;left:80px;top:301px;display:flex;gap:5px}
.fsocial span{width:42px;height:35px;background:var(--navy-field);display:flex;align-items:center;justify-content:center}
.fsocial i{width:9px;height:9px;border-radius:50%;background:var(--white)}
.fhead{position:absolute;top:82px;font-size:20px;font-weight:700;color:var(--white)}
.fhead::after{content:"";position:absolute;left:0;top:38px;width:44px;height:3px;background:var(--red)}
.flinks{position:absolute;top:145px;font-size:14px;color:#e4ebf4;display:flex;flex-direction:column;gap:15.5px}
.fnote{position:absolute;left:787px;top:145px;font-size:14px;color:#e4ebf4}
.field{position:absolute;left:787px;top:173px;width:330px;height:40px;background:var(--navy-field);color:#e4ebf4;font-size:14px;padding:13px 27px}
.subscribe{position:absolute;left:787px;top:218px;width:330px;height:40px;background:var(--red);color:var(--white);font-size:14px;font-weight:500;display:flex;align-items:center;justify-content:center;border-radius:2px}
.divider{position:absolute;left:0;top:419px;width:1200px;height:1px;background:rgba(255,255,255,.08)}
.copy{position:absolute;left:0;top:444px;width:1200px;text-align:center;font-size:14px;color:#e4ebf4}
</style>
</head>
<body>

<header class="abs topbar">
  <div class="item" style="left:88px">
    <svg width="12" height="9" viewBox="0 0 12 9"><rect width="12" height="9" rx="1"/></svg>
    E-mail: contact@halvernpainting.com
  </div>
  <div class="item" style="left:336px">
    <svg width="12" height="12" viewBox="0 0 12 12"><circle cx="6" cy="6" r="5" fill="none" stroke="#dfe8f3" stroke-width="1.5"/><path d="M6 3v3.3l2 1.2" stroke="#dfe8f3" stroke-width="1.3" fill="none"/></svg>
    Hours: Mon-Fri: 8.00 am - 7.00 pm
  </div>
  <div class="item" style="left:890px">
    <svg width="11" height="11" viewBox="0 0 12 12"><path d="M2.5 1l2 2.4-1.2 1.4c.8 1.6 2.1 2.9 3.7 3.7l1.4-1.2L11 9.5 9.6 11C5 10.6 1.4 7 1 2.4z"/></svg>
    + 555-014-0277
  </div>
  <div class="item" style="left:1020px;gap:12px"><span class="social-dot"></span><span class="social-dot"></span><span class="social-dot"></span><span class="social-dot"></span></div>
</header>

<nav class="abs nav">
  <div class="brand">HALVERN PAINTING<span class="mark"></span></div>
  <div class="menu"><span>Home</span><span>About</span><span>Residential</span><span>Multi-Family</span><span>Commercial</span><span>Contact</span></div>
  <div class="estimate">GET A FREE ESTIMATE</div>
</nav>

<section class="abs hero" role="img" aria-label="Dimmed photo of a freshly painted white kitchen interior">
  <h1>Our Services</h1>
  <div class="crumbs"><span>Home</span><span>.</span><span>Services</span><span>.</span><b>Details</b></div>
</section>

<div class="abs num" style="left:42px;top:420px">01</div>
<div class="abs photo" style="left:86px;top:479px;width:501px;height:375px;background:linear-gradient(160deg,#d9d9d6,#b9b8b3 55%,#5e5348)" role="img" aria-label="Bright kitchen with white cabinets, island and pendant lights"></div>
<div class="abs svc" style="left:640px;top:480px">
  <h2>Residential Painting</h2>
  <p class="lead">Lorem ipsum dolor sit amet, consectetur adipiscing elit, sed do eiusmod</p>
  <p class="body">Neque porro quisquam est, qui dolorem ipsum quia dolor sit amet they consec tetur, adipisci velit, sed quia non numquam eius modi tempora incidunt ut labore et dolore magnam aliquam quaerat voluptatemo qui quia dolor sit amedipisci develit.</p>
  <div class="btn">LEARN MORE <span>›</span></div>
</div>

<div class="abs num" style="left:1012px;top:858px">02</div>
<div class="abs svc" style="left:86px;top:918px">
  <h2>Commercial Painting</h2>
  <p class="lead">Lorem ipsum dolor sit amet, consectetur adipiscing elit, sed do eiusmod</p>
  <p class="body">Neque porro quisquam est, qui dolorem ipsum quia dolor sit amet they consec tetur, adipisci velit, sed quia non numquam eius modi tempora incidunt ut labore et dolore magnam aliquam quaerat voluptatemo qui quia dolor sit amedipisci develit.</p>
  <div class="btn">LEARN MORE <span>›</span></div>
</div>
<div class="abs photo" style="left:613px;top:917px;width:500px;height:374px;background:linear-gradient(180deg,#3a3a3c,#6b6e78 40%,#7d7f83 70%,#6a6b6e)" role="img" aria-label="Commercial fitness studio with a painted mural wall and grey floor"></div>

<div class="abs num" style="left:42px;top:1295px">03</div>
<div class="abs photo" style="left:86px;top:1353px;width:501px;height:438px;background:linear-gradient(180deg,#5f8fc4,#6b7d6a 30%,#8b4a33 60%,#7a3f2c)" role="img" aria-label="Red brick multi-family home with white trim under a blue sky"></div>
<div class="abs svc" style="left:640px;top:1354px">
  <h2>Multi-Family Painting</h2>
  <p class="lead">Lorem ipsum dolor sit amet, consectetur adipiscing elit, sed do eiusmod</p>
  <p class="body">Neque porro quisquam est, qui dolorem ipsum quia dolor sit amet they consec tetur, adipisci velit, sed quia non numquam eius modi tempora incidunt ut labore et dolore magnam aliquam quaerat voluptatemo qui quia dolor sit amedipisci develit.</p>
  <div class="btn">LEARN MORE <span>›</span></div>
</div>

<section class="abs cta">
  <h3>Get Your Painting Project Started Today!</h3>
  <div class="quote">GET A QUOTE <span>›</span></div>
</section>

<footer class="abs footer">
  <div class="flogo">HALVERN<span class="mark"></span></div>
  <p class="fabout">Lorem ipsum dolor sit amet, consectetur adipiscing elit, sed do eiusmod tempor incididunt ut labore et dolore magna aliqua.</p>
  <div class="fsocial"><span><i></i></span><span><i></i></span><span><i></i></span><span><i></i></span><span><i></i></span></div>

  <div class="fhead" style="left:432px">Quick Links</div>
  <div class="flinks" style="left:432px"><span>Home</span><span>About Us</span><span>Residential</span><span>Commercial</span><span>Multi Family</span></div>
  <div class="flinks" style="left:635px"><span>Site Map</span><span>Maintenance</span><span>Repairs</span><span>Blog</span></div>

  <div class="fhead" style="left:787px">Newsletter</div>
  <div class="fnote">Subscribe For Daily Latest News &amp; Updates</div>
  <div class="field">E-mail Address</div>
  <div class="subscribe">Subscribe Now</div>

  <div class="divider"></div>
  <div class="copy">Copyright © 2020 Halvern Painting. All Rights Reserved.</div>
</footer>

</body>
</html>
```